Banner Ads for Online Poker Promotion

We are an online poker network, the KLV (www.theklvnet.eu). We are looking for a small selection of web banner ads for our latest promotion.

Banner sizes that we need are:
- 196x523 (static .psd and .png)
- 199x129 (static .psd and .png)
- 447x426 (static .psd and .png)
- 500x400 (static .psd and .png)
- 697x167 (static .psd and .png)
- 460x60 (animated .gif)

The promotion name is ‘Rush & Deal Plunder’ (or ‘RND Plunder’) and the concept is that certain Sit & Go tournaments have money added to the prize pool. Basically, free cash for Sit & Go players.

(If you don’t know poker, a ‘Sit & Go’ is a tournament which starts when a specific number of players join, as opposed to a scheduled tournament which starts at a specific time).

The promotion starts on November 3rd.

Guidelines:

The name of the promotion, ‘Rush & Deal Plunder’ or ‘RND Plunder’, should feature prominently in the banners.

The strap line can be ‘Get Your Share of the Loot’, ‘Added Money in SNGs’ or something similar (feel free to be creative).

Our network logo (attached) must feature on the animated .gif. It is optional on the other banners.

Examples of past promotional imagery can be found on our website, in particular these pages: http://www.theklvnet.eu/promotions/ and http://www.theklvnet.eu/promotions/archived-promotions/ . Our last promotion was crowdsourced and the details of that and the winner can be found here: http://jobs.artquarry.com/job.aspx?id=512047

We are looking to go in a more modern and risqué direction than the past, in order to stand out from competition which is very bland.

Common poker imagery –cards, chips, suit icons etc – or objects associated with live poker (tables, etc) is a little clichéd. It can be included if it has a clear purpose. But don’t just put flying cards or suit symbols in there for no reason.

More like vexOS4/5, less like vexOS3

Think flat, modern, glamour, clean, fresh, bright, rock music, extreme sports, and the Loud Stone!

Most of our customers are 18-35, male, and we have a strong European focus.

As we are a gaming company, the banners must not encourage underage play, problem gambling, or associate gambling with sexual or social success.

If any further guidance is needed please don’t hesitate to ask!

```html
<!DOCTYPE html>
<html lang="en">
<head>
<meta charset="utf-8">
<title>RND Plunder – Banner 500x400</title>
<link rel="stylesheet" href="https://fonts.googleapis.com/css2?family=Oswald:wght@500;700&family=Lobster&display=swap">
<style>
  :root {
    --curtain-deep: #3a0608;
    --curtain-red: #8e1a1c;
    --curtain-glow: #c8433a;
    --gold-light: #fff3c9;
    --gold-mid: #e9c77a;
    --gold-deep: #a9782f;
    --gold-dark: #6b4718;
    --band-dark: #1c140c;
    --ink-white: #ffffff;
  }
  html, body {
    margin: 0;
    padding: 0;
    width: 1200px;
    height: 960px;
    overflow: hidden;
    background: var(--curtain-deep);
  }
  .banner {
    position: relative;
    width: 1200px;
    height: 960px;
    overflow: hidden;
  }
  .stage-backdrop {
    position: absolute;
    inset: 0;
    background:
      radial-gradient(ellipse 55% 45% at 50% 48%, var(--curtain-glow) 0%, transparent 70%),
      linear-gradient(180deg, var(--curtain-red) 0%, var(--curtain-deep) 100%);
  }
  .frame-corner {
    position: absolute;
    width: 250px;
    height: 340px;
    background: linear-gradient(150deg, var(--gold-light) 0%, var(--gold-deep) 55%, var(--gold-dark) 100%);
    opacity: 0.85;
  }
  .frame-corner--left { left: 0; top: 0; border-bottom-right-radius: 100% 60%; }
  .frame-corner--right { right: 0; top: 0; border-bottom-left-radius: 100% 60%; }
  .stage-props {
    position: absolute;
    left: 170px;
    top: 220px;
    width: 860px;
    height: 620px;
    border-radius: 40% 40% 30% 30%;
    background: radial-gradient(ellipse at 50% 45%, #d9c6b8 0%, #a8433c 45%, rgba(90,14,16,0) 75%);
  }
  .presenter {
    position: absolute;
    top: 24px;
    left: 0;
    width: 100%;
    display: flex;
    justify-content: center;
    align-items: center;
    gap: 12px;
    font-family: "Oswald", sans-serif;
    font-weight: 500;
    font-size: 42px;
    color: var(--ink-white);
    letter-spacing: 1px;
  }
  .presenter__mark {
    width: 26px;
    height: 26px;
    border-radius: 50%;
    background: var(--ink-white);
  }
  .title {
    position: absolute;
    left: 0;
    width: 100%;
    text-align: center;
    margin: 0;
    background: linear-gradient(180deg, var(--gold-light) 0%, var(--gold-mid) 45%, var(--gold-deep) 100%);
    -webkit-background-clip: text;
    background-clip: text;
    color: transparent;
  }
  .title--short {
    top: 240px;
    font-family: "Oswald", sans-serif;
    font-weight: 700;
    font-size: 110px;
    line-height: 1;
    letter-spacing: 4px;
  }
  .title--name {
    top: 380px;
    font-family: "Lobster", cursive;
    font-weight: 400;
    font-size: 290px;
    line-height: 1.2;
    filter: drop-shadow(0 6px 8px rgba(40, 5, 5, 0.6));
  }
  .strap {
    position: absolute;
    left: 72px;
    right: 72px;
    bottom: 0;
    height: 88px;
    box-sizing: border-box;
    border: 4px solid var(--gold-mid);
    border-bottom: none;
    background: var(--band-dark);
    display: flex;
    align-items: center;
    justify-content: center;
  }
  .strap__text {
    margin: 0;
    font-family: "Oswald", sans-serif;
    font-weight: 700;
    font-size: 50px;
    letter-spacing: 1px;
    text-transform: uppercase;
    color: var(--gold-mid);
  }
</style>
</head>
<body>
  <div class="banner">
    <div class="stage-backdrop" role="img" aria-label="Red theatre stage curtains with warm spotlight glow"></div>
    <div class="frame-corner frame-corner--left" role="img" aria-label="Ornate gold baroque frame corner"></div>
    <div class="frame-corner frame-corner--right" role="img" aria-label="Ornate gold baroque frame corner"></div>
    <div class="stage-props" role="img" aria-label="Vintage microphone, scattered playing cards, bottles and a disco ball"></div>

    <div class="presenter">
      <span class="presenter__mark"></span>
      <span class="presenter__text">KLV PRESENTS</span>
    </div>

    <p class="title title--short">RND</p>
    <h1 class="title title--name">Plunder</h1>

    <div class="strap">
      <p class="strap__text">Get your share of the loot!</p>
    </div>
  </div>
</body>
</html>
```